Brennick Capital Business Cards

These are professional business cards that are for my family office.
Put fake emails and phone numbers as of now until I finalize those components. This family office controls my families investments, assets, and future. The cards should be professional.
..
.
.
.
I just uploaded another variation of a logo I would like to see as a business card to I am inbeteen which logo to use

Target Market(s)

business

Industry/Entity Type

business

Contact Information for Business Card

Professional, wealth related, finance related.

Requirements
Must have
• Logo

```html
<!DOCTYPE html>
<html lang="en">
<head>
<meta charset="utf-8">
<title>Brennick Capital Business Cards</title>
<link rel="stylesheet" href="https://fonts.googleapis.com/css2?family=Bodoni+Moda:wght@500&family=Arimo:wght@400&display=swap">
<style>
  :root {
    --backdrop-light: #d4d4d4;
    --backdrop-dark: #a4a4a4;
    --card: #272727;
    --card-deep: #1d1d1d;
    --gold: #c6ab6e;
    --white: #ffffff;
    --ink-soft: #e9e9e9;
  }
  * { margin: 0; padding: 0; box-sizing: border-box; }
  html, body { width: 1200px; height: 788px; overflow: hidden; }
  body {
    background: radial-gradient(ellipse at 30% 10%, var(--backdrop-light), var(--backdrop-dark));
    position: relative;
  }
  .card {
    position: absolute;
    width: 540px;
    height: 310px;
    border-radius: 22px;
    overflow: hidden;
    box-shadow: 0 18px 40px rgba(0,0,0,0.28);
  }
  .card--front { left: 40px; top: 239px; background: var(--card); }
  .card--back {
    left: 620px; top: 239px;
    background: linear-gradient(135deg, #2c2c2c 0%, var(--card-deep) 100%);
    display: flex; align-items: center; justify-content: center;
  }
  .company-name {
    font-family: "Arimo", sans-serif;
    font-weight: 400;
    color: var(--white);
    letter-spacing: 0.01em;
    white-space: nowrap;
  }
  .card--front .company-name { position: absolute; left: 44px; top: 46px; font-size: 28px; }
  .card--back .company-name { font-size: 40px; }

  .person { position: absolute; left: 44px; top: 140px; width: 200px; }
  .person__name {
    font-family: "Bodoni Moda", serif; font-weight: 500;
    color: var(--gold); font-size: 22px; letter-spacing: 0.05em; text-transform: uppercase;
    white-space: nowrap;
  }
  .person__title {
    font-family: "Arimo", sans-serif; color: var(--ink-soft);
    font-size: 16px; margin-top: 4px; text-align: right;
  }
  .divider {
    position: absolute; left: 262px; top: 126px;
    width: 1px; height: 84px; background: var(--gold);
  }
  .contacts { position: absolute; left: 282px; top: 124px; list-style: none; }
  .contacts li {
    display: flex; align-items: center; gap: 8px;
    font-family: "Arimo", sans-serif; color: var(--ink-soft);
    font-size: 14px; line-height: 28px; white-space: nowrap;
  }
  .contacts svg { width: 12px; height: 12px; fill: var(--gold); flex: none; }
  .address {
    position: absolute; left: 44px; top: 250px;
    font-family: "Arimo", sans-serif; color: var(--ink-soft); font-size: 15px;
    white-space: nowrap;
  }
  .edge-band { position: absolute; left: 0; bottom: 0; width: 540px; height: 9px; }
</style>
</head>
<body>
  <section class="card card--front">
    <div class="company-name">Brennick Capital</div>
    <div class="person">
      <div class="person__name">Elliot Marsh</div>
      <div class="person__title">CEO/Founder</div>
    </div>
    <div class="divider"></div>
    <ul class="contacts">
      <li><svg viewBox="0 0 12 12"><path d="M2.5 1h2l1 2.5-1.3 1a6 6 0 0 0 3.3 3.3l1-1.3 2.5 1v2a1 1 0 0 1-1 1A9.5 9.5 0 0 1 1.5 2a1 1 0 0 1 1-1z"/></svg>(555) 018-4420</li>
      <li><svg viewBox="0 0 12 12"><path d="M1 2.5h10v7H1z M1.5 3l4.5 3.5L10.5 3" stroke="#272727" stroke-width="0.9"/></svg>ElliotM@brennickcapital.com</li>
      <li><svg viewBox="0 0 12 12"><circle cx="6" cy="6" r="5"/><path d="M1 6h10M6 1c-2.5 3-2.5 7 0 10M6 1c2.5 3 2.5 7 0 10" stroke="#272727" stroke-width="0.8" fill="none"/></svg>www.brennickcapital.com</li>
    </ul>
    <div class="address">4870 N. Larkspur Ave Suite 200 Harlow, AB 602318</div>
    <svg class="edge-band" viewBox="0 0 540 9" preserveAspectRatio="none">
      <rect x="0" y="0" width="540" height="9" fill="var(--gold)"/>
      <polygon points="0,0 236,0 230,9 0,9" fill="var(--white)"/>
    </svg>
  </section>

  <section class="card card--back">
    <div class="company-name">Brennick Capital</div>
  </section>
</body>
</html>
```